Window Advertisment for Rentals Company

I own a property rental company in Cyprus and I am looking for an eye catching design to place in my window to attract passers by.

Please check the attachment for more details.

Ad size to be 309cm x 204cm landscape

The font of the logo is velocity

Target Market(s)

Property Owners

Industry/Entity Type

It Company

Requirements
Must have
• The colours from my logo and be eye catching and make passers by take notice

```html
<!DOCTYPE html>
<html lang="en">
<head>
<meta charset="utf-8">
<title>Solvista Stays – Owners Wanted</title>
<link href="https://fonts.googleapis.com/css2?family=Open+Sans:wght@700;800&display=swap" rel="stylesheet">
<style>
  :root{
    --orange:#f07023;
    --yellow:#fcc10c;
    --red:#e8141c;
    --white:#ffffff;
    --shield:#ebebeb;
    --sky:#9fc3e6;
    --wall:#efe6d8;
    --pool:#3cc4ee;
  }
  *{margin:0;padding:0;box-sizing:border-box}
  html,body{width:1200px;height:1200px;overflow:hidden;background:var(--white)}
  body{font-family:"Open Sans",Arial,sans-serif;position:relative}
  .poster{position:absolute;inset:0}
  .shapes{position:absolute;inset:0}
  .headline{position:absolute;left:0;top:204px;width:1200px;height:260px;text-align:center;color:var(--white)}
  .headline h1{font-weight:800;font-size:77px;line-height:88px;letter-spacing:0.5px;padding-top:26px;padding-left:0}
  .headline p{font-weight:700;font-size:32px;line-height:38px;margin-top:4px;padding-left:8px}
  .brand{position:absolute;left:408px;top:520px;width:308px;text-align:center;color:var(--orange);font-weight:800;font-size:40px;line-height:46px}
  .benefits{position:absolute;left:30px;top:0;list-style:none}
  .benefits li{position:absolute;left:0;width:680px;display:flex;align-items:flex-start;color:var(--red);font-weight:700;font-size:27px;line-height:34px;white-space:nowrap}
  .benefits li svg{flex:none;width:58px;height:48px;margin-right:6px;margin-top:-14px}
  .benefits li.two-line{white-space:normal;width:660px}
  .contact{position:absolute;top:928px;height:68px;display:flex;align-items:center;color:var(--white);font-weight:800}
  .contact.web{left:10px;font-size:27px}
  .contact.web small{font-size:20px}
  .contact.tel{left:524px;font-size:33px}
</style>
</head>
<body>
<div class="poster">
  <svg class="shapes" width="1200" height="1200" viewBox="0 0 1200 1200">
    <defs>
      <linearGradient id="villaTones" x1="0" y1="0" x2="0" y2="1">
        <stop offset="0" stop-color="var(--sky)"/>
        <stop offset="0.25" stop-color="var(--wall)"/>
        <stop offset="0.6" stop-color="#d9cdb9"/>
        <stop offset="0.75" stop-color="var(--pool)"/>
        <stop offset="1" stop-color="#d8cbb5"/>
      </linearGradient>
    </defs>
    <rect class="top-band" x="0" y="204" width="1200" height="260" fill="var(--orange)"/>
    <path class="bottom-band" d="M0 928H800V996H0Z" fill="var(--orange)"/>
    <path class="band-divider" d="M468 928H480L504 996H492Z" fill="var(--yellow)"/>
    <path class="logo-shield" d="M408 464H716V584L564 712L408 584Z" fill="var(--shield)"/>
    <path class="photo-edge" d="M796 464H816L712 720L820 996H800L692 720Z" fill="var(--yellow)"/>
    <path class="villa-photo" role="img" aria-label="Photo of a white two-storey villa with balcony, patio and swimming pool" d="M816 464H1200V996H820L712 720Z" fill="url(#villaTones)"/>
  </svg>

  <header class="headline">
    <h1>WE ARE LOOKING FOR<br>VILLAS AND APARTMENTS</h1>
    <p>TO FULFILL OUR GROWING DEMAND OF RENTALS</p>
  </header>

  <div class="brand">Solvista<br>Stays</div>

  <ul class="benefits">
    <li style="top:524px"><svg viewBox="0 0 58 48"><rect x="2" y="10" width="40" height="36" fill="none" stroke="var(--red)" stroke-width="2"/><path d="M8 26L20 40L54 4L20 32Z" fill="var(--red)"/></svg>LOW COMMISSIONS</li>
    <li style="top:592px"><svg viewBox="0 0 58 48"><rect x="2" y="10" width="40" height="36" fill="none" stroke="var(--red)" stroke-width="2"/><path d="M8 26L20 40L54 4L20 32Z" fill="var(--red)"/></svg>QUICK PAYOUTS</li>
    <li style="top:672px"><svg viewBox="0 0 58 48"><rect x="2" y="10" width="40" height="36" fill="none" stroke="var(--red)" stroke-width="2"/><path d="M8 26L20 40L54 4L20 32Z" fill="var(--red)"/></svg>FREE ADVERTISING</li>
    <li style="top:736px"><svg viewBox="0 0 58 48"><rect x="2" y="10" width="40" height="36" fill="none" stroke="var(--red)" stroke-width="2"/><path d="M8 26L20 40L54 4L20 32Z" fill="var(--red)"/></svg>CONNECT WITH OVER 35 LEADING WEBSITES</li>
    <li class="two-line" style="top:814px"><svg viewBox="0 0 58 48"><rect x="2" y="10" width="40" height="36" fill="none" stroke="var(--red)" stroke-width="2"/><path d="M8 26L20 40L54 4L20 32Z" fill="var(--red)"/></svg><span>BE SEEN BY 100+ MILLION TRAVELLERS PER MONTH!</span></li>
  </ul>

  <div class="contact web">www.SOLVISTASTAYS<small>.com</small></div>
  <div class="contact tel">TEL: 24 555018</div>
</div>
</body>
</html>
```